Zielgruppe
Wir vermieten Köche und Küchenhilfen an unsere Kunden. Die Visitenkarten sind sowohl für potentielle Neukunden als auch potentielle neue Mitarbeitern.
Aufgabenstellung
Unsere Visitenkarten sollen modern sein ohne zu voll zu wirken.
Auf ihr enthalten sollen sein: Logo, Name, Position, Telefonnr (Festnetz und Mobil), Adresse, Email und Logo.
Ein kurzer, knapper Motivationsspruch wäre auch schön.

```html
<!DOCTYPE html>
<html lang="de">
<head>
<meta charset="utf-8">
<title>Tarvo Catering – Visitenkarten</title>
<link rel="stylesheet" href="https://fonts.googleapis.com/css2?family=Fira+Sans:ital,wght@0,400;0,500;0,700;1,400&display=swap">
<style>
:root{
  --backdrop:#2c2c2e;
  --card:#ffffff;
  --ink:#3a3a40;
  --accent:#e8582a;
  --bar:#4a4a52;
}
*{box-sizing:border-box;margin:0;padding:0}
html,body{width:1200px;height:2323px;overflow:hidden}
body{background:var(--backdrop);font-family:"Fira Sans",sans-serif;color:var(--ink);position:relative}
.card{position:absolute;width:437px;height:676px;background:var(--card);overflow:hidden}
.card > *{position:absolute;left:0;right:0;text-align:center}
.front-quote{left:121px;top:98px}
.back-plain{left:634px;top:98px}
.front-photo{left:121px;top:838px}
.back-photo{left:634px;top:838px}
.back-accent{left:388px;top:1560px}
.mark{left:50%;right:auto;border-radius:50%;background:var(--ink);transform:translateX(-50%)}
.brand{font-weight:500;font-variant:small-caps;letter-spacing:3px;color:var(--ink)}
.quote{font-style:italic;font-size:21px;line-height:27px}
.quote-author{font-size:15px;color:var(--accent)}
.url{font-size:23px;color:var(--accent)}
.person{font-weight:700;font-variant:small-caps;font-size:30px;letter-spacing:.5px}
.role,.address{font-variant:small-caps;font-size:19px;letter-spacing:1px;line-height:24px}
.phones{font-variant:small-caps;font-size:19px;letter-spacing:.8px;line-height:23px;color:var(--accent)}
.email{font-variant:small-caps;font-size:16px;letter-spacing:1px}
.photo-band{height:162px;background:linear-gradient(100deg,#6c4e2a 0%,#b88a4c 30%,#e7e4df 60%,#5b5d66 100%)}
.event-band{top:526px;height:111px;background:linear-gradient(90deg,#d8d4d2 0%,#8b8690 35%,#3d3340 55%,#7a3a8e 75%,#c0609a 100%)}
.mark-ring{border:7px solid var(--card)}
.accent-panel{top:163px;height:441px;background:var(--accent)}
.accent-panel,.accent-panel *{color:#fff}
.divider{top:604px;height:16px;background:var(--bar)}
.tagline{font-weight:700;font-variant:small-caps;font-size:19px;color:var(--accent);letter-spacing:.5px}
</style>
</head>
<body>

<section class="card front-quote">
  <div class="mark" style="top:92px;width:88px;height:88px"></div>
  <div class="brand" style="top:200px;font-size:40px">Tarvo Catering</div>
  <p class="quote" style="top:372px">“Gutes Essen kann<br>gesundheitsschädlich sein,<br>schlechtes ist es immer.”</p>
  <p class="quote-author" style="top:462px">– Konrad Almeier</p>
  <p class="url" style="top:611px">www.tarvo-catering.de</p>
</section>

<section class="card back-plain">
  <div class="mark" style="top:93px;width:68px;height:68px"></div>
  <div class="brand" style="top:172px;font-size:30px">Tarvo Catering</div>
  <p class="person" style="top:314px">Vorname Nachname</p>
  <p class="role" style="top:356px">Geschäftsführer</p>
  <p class="address" style="top:408px">Ahorn-Weber-Strasse 16<br>61240 Feldhausen</p>
  <p class="phones" style="top:481px">Festnetz: 0175 / 4820917<br>Mobile:&nbsp;&nbsp;&nbsp;&nbsp;0175 / 4820917</p>
  <p class="email" style="top:553px">info@tarvo-catering.de</p>
</section>

<section class="card front-photo">
  <div class="photo-band" role="img" aria-label="Foto: Koch rührt in einem Kupfertopf"></div>
  <div class="mark mark-ring" style="top:140px;width:108px;height:108px"></div>
  <div class="brand" style="top:268px;font-size:44px">Tarvo Catering</div>
  <p class="url" style="top:592px">www.tarvo-catering.de</p>
</section>

<section class="card back-photo">
  <div class="mark" style="top:59px;width:60px;height:60px"></div>
  <div class="brand" style="top:128px;font-size:28px">Tarvo Catering</div>
  <p class="person" style="top:228px">Vorname Nachname</p>
  <p class="role" style="top:270px">Geschäftsführer</p>
  <p class="address" style="top:322px">Ahorn-Weber-Strasse 16<br>61240 Feldhausen</p>
  <p class="phones" style="top:395px">Festnetz: 0175 / 4820917<br>Mobile:&nbsp;&nbsp;&nbsp;&nbsp;0175 / 4820917</p>
  <p class="email" style="top:467px">info@tarvo-catering.de</p>
  <div class="event-band" role="img" aria-label="Fotostreifen: gedeckte Festtafel, Mikrofon und Konzertpublikum"></div>
</section>

<section class="card back-accent">
  <div class="mark" style="top:21px;width:56px;height:56px"></div>
  <div class="brand" style="top:86px;font-size:28px">Tarvo Catering</div>
  <div class="accent-panel">
    <p class="person" style="position:absolute;left:0;right:0;top:58px">Vorname Nachname</p>
    <p class="role" style="position:absolute;left:0;right:0;top:102px">Geschäftsführer</p>
    <p class="address" style="position:absolute;left:0;right:0;top:160px">Ahorn-Weber-Strasse 16<br>61240 Feldhausen</p>
    <p class="phones" style="position:absolute;left:0;right:0;top:234px;font-weight:700;font-size:20px;line-height:27px">Tel. 0175 / 4820917<br>Mobile: 0175 / 4820917</p>
    <p class="email" style="position:absolute;left:0;right:0;top:317px">info@tarvo-catering.de</p>
  </div>
  <div class="divider"></div>
  <p class="tagline" style="top:633px">Event – Personal – Ihr Spezialist</p>
</section>

</body>
</html>
```